brivox new business card design project

we need a new business card design. you can view info about us @ brivox.com. i have attached an example of our previous card with our previous name that we no longer use. We really liked the design, colors etc. look below to see more info about this project. it asks for a limited number of words. please see our website for more info about our compnay.

Target Market(s)

law enforcement

Contact Information for Business Card

i have uploaded an example of what we used before that we liked.

Font styles to use
Serif

```html
<!DOCTYPE html>
<html lang="en">
<head>
<meta charset="utf-8">
<title>Brivox Business Card</title>
<link rel="stylesheet" href="https://fonts.googleapis.com/css2?family=Exo+2:wght@300&family=Roboto:ital,wght@0,300;0,400;1,300&display=swap">
<style>
  :root {
    --page-bg: #e9e9e9;
    --card-dark: #0a1620;
    --brand-blue: #1a74b8;
    --brand-blue-deep: #0e5c99;
    --ink-light: #e8edf2;
    --ink-soft: #c9d7e4;
    --divider: #f2f2f2;
  }
  * { margin: 0; padding: 0; box-sizing: border-box; }
  html, body { width: 1200px; height: 576px; overflow: hidden; }
  body {
    background: var(--page-bg);
    position: relative;
    font-family: "Roboto", sans-serif;
  }
  .card {
    position: absolute;
    top: 138px;
    width: 484px;
    height: 292px;
    border-radius: 14px;
    overflow: hidden;
    background: var(--card-dark);
  }
  .card--front { left: 82px; }
  .card--back { left: 602px; }

  .network-map {
    position: absolute;
    left: 28px; top: 26px;
    width: 420px; height: 240px;
    background: radial-gradient(ellipse at 50% 50%, rgba(40,80,110,0.35) 0%, rgba(20,45,65,0.2) 45%, rgba(10,22,32,0) 75%);
  }
  .wordmark {
    position: absolute;
    left: 0; right: 0;
    text-align: center;
    font-family: "Exo 2", sans-serif;
    font-weight: 300;
    color: var(--ink-light);
    letter-spacing: 4px;
  }
  .card--front .wordmark { top: 92px; font-size: 60px; }
  .card--back .wordmark { top: 28px; font-size: 54px; }

  .front-stripes { position: absolute; left: 0; bottom: 0; }
  .front-url {
    position: absolute;
    right: 26px; bottom: 9px;
    font-size: 12px;
    letter-spacing: 3.2px;
    color: var(--ink-light);
  }

  .tagline {
    position: absolute;
    top: 88px; left: 0; right: 0;
    text-align: center;
    font-size: 12px;
    letter-spacing: 1.2px;
    color: var(--ink-light);
  }
  .tagline .sep { color: var(--brand-blue); margin: 0 6px; }

  .back-wave { position: absolute; left: 0; top: 0; }

  .holder {
    position: absolute;
    left: 58px; top: 186px;
    width: 190px;
    text-align: center;
  }
  .holder-name { font-size: 20px; font-weight: 400; color: #fff; }
  .holder-role { font-size: 12px; font-style: italic; font-weight: 300; color: var(--ink-soft); margin-top: 5px; }

  .contact-list {
    position: absolute;
    left: 246px; top: 183px;
    list-style: none;
  }
  .contact-list li {
    display: flex; align-items: center;
    height: 17px;
    font-size: 12.5px; font-weight: 300;
    color: var(--ink-light);
  }
  .contact-list svg { width: 11px; height: 11px; margin-right: 11px; }
  .address {
    position: absolute;
    left: 0; right: 0; top: 253px;
    text-align: center;
    font-size: 12.5px; font-weight: 300;
    color: var(--ink-light);
  }
</style>
</head>
<body>

<section class="card card--front">
  <div class="network-map" role="img" aria-label="Faint network map of the United States with connected points"></div>
  <div class="wordmark">BRIVOX</div>
  <svg class="front-stripes" width="340" height="24" viewBox="0 0 340 24">
    <polygon points="0,0 194,0 182,24 0,24" fill="var(--brand-blue)"/>
    <polygon points="217,0 271,0 259,24 205,24" fill="#e6e6e6"/>
  </svg>
  <div class="front-url">www.brivox.com</div>
</section>

<section class="card card--back">
  <svg class="back-wave" width="484" height="292" viewBox="0 0 484 292">
    <defs>
      <linearGradient id="blueFill" x1="0" y1="0" x2="0" y2="1">
        <stop offset="0" stop-color="var(--brand-blue)"/>
        <stop offset="1" stop-color="var(--brand-blue-deep)"/>
      </linearGradient>
    </defs>
    <path d="M0,112 Q242,210 484,112 L484,292 L0,292 Z" fill="url(#blueFill)"/>
    <path d="M0,112 Q242,210 484,112" fill="none" stroke="var(--divider)" stroke-width="3"/>
  </svg>
  <div class="wordmark">BRIVOX</div>
  <div class="tagline">Smarter Systems<span class="sep">|</span>Stronger Support</div>

  <div class="holder">
    <div class="holder-name">Daniel Harwick</div>
    <div class="holder-role">Founder/Chief Exe. Officer</div>
  </div>

  <ul class="contact-list">
    <li>
      <svg viewBox="0 0 12 12"><path d="M1,4 Q6,0 11,4 L10,5.5 L8,4.5 L8,3.5 Q6,2.8 4,3.5 L4,4.5 L2,5.5 Z M3,6 L9,6 L10.5,11 L1.5,11 Z" fill="var(--ink-light)"/></svg>
      555.210.4470
    </li>
    <li>
      <svg viewBox="0 0 12 12"><rect x="0.5" y="2" width="11" height="8" fill="none" stroke="var(--ink-light)" stroke-width="1.2"/><path d="M0.5,2 L6,7 L11.5,2" fill="none" stroke="var(--ink-light)" stroke-width="1.2"/></svg>
      info@brivox.com
    </li>
    <li>
      <svg viewBox="0 0 12 12"><circle cx="6" cy="6" r="5" fill="none" stroke="var(--ink-light)" stroke-width="1"/><ellipse cx="6" cy="6" rx="2.2" ry="5" fill="none" stroke="var(--ink-light)" stroke-width="0.9"/><line x1="1" y1="6" x2="11" y2="6" stroke="var(--ink-light)" stroke-width="0.9"/></svg>
      www.brivox.com
    </li>
  </ul>

  <div class="address">1420 Larkfield Avenue Austin, TX 78701</div>
</section>

</body>
</html>
```